Stationary for Beauty and Spa School

Create a business card, letterhead and envelopes (primarily #10 envelope with and without window and catalog envelope) for a beauty and wellness school in Miami, Fl. We offer 8 different programs of study and need an eye catching look. Looking for a combination of modern yet sophisticated. Nothing corporate or business looking. Would like to have a look and feel that is similar (or incorporates aspects) of a new website we will be launching in the next 30 days (screen shot attached.)

The final design should communicate style and elegance in a down to earth and friendly way. We strive to provide our students with quality education, friendly and amicable staff and experienced instructors.
Updates

Hello. FYI, in order to print an aesthetically appealing business card, we would like to print them (the business cards) using silk printing method, with spot UV coating (on some elements, maybe the logo, or depending on the design) and die cuts. Please think of this when preparing your design.

Only 1 day left, please submit your designs for selection. Thanks

Target Market(s)

Adults 18-49 years who are mostly interested in beauty and fashion. Need a youthful & modern look, yet sophisticated and elegant.

Industry/Entity Type

School

Colors
e34197
6b449b
add136
f79021

Requirements
Must have
• Similar look and feel as website (see attached screen shot)
Same look and feel of website (see attached screenshot)
Logo
Address: 5126 NW 14th Avenue. Miami, Fl 33157
Telephone: 305-914-3062
Fax: 786-552-4190
website/url: www.lumaroveacademy.edu
incorporate Photo of blonde model (attached)
Nice to have
• Tag line: "Beautify your future." Also, maybe two-sided business card. Would be nice if we could mention our programs (maybe in the back of the card). Below are the program offerings (names cannot be changed but order is irrelevant)... Cosmetology, Barber, Spa Therapy, Massage Therapy, Makeup Artistry, Skin Care, Manicure, Pedicure & Nail Extensions, Full Specialist.

A design with text plus a beautiful photo of a model is appealing. Attached to the files is a sample of a cover for a student handbook we have created. You should use the photo of the blonde model (attached) in your design. The original (quality) version of this stock photograph has been uploaded.

Also would be nice to request clients to follow us on facebook and instagram by including the icons.
Should not have
• A corporate or business look. We are a vocational school teaching beauty and spa programs and we like our advertising to have a look that resembles the industry. We do not want a very serious look or snobby feel.

```html
<!DOCTYPE html>
<html lang="en">
<head>
<meta charset="utf-8">
<title>Lumarove Academy — Business Cards</title>
<link rel="stylesheet" href="https://fonts.googleapis.com/css2?family=Open+Sans:wght@400;600;700&family=Courgette&display=swap">
<style>
  :root {
    --bg: #e9e9ee;
    --card: #ffffff;
    --band: #b5479a;
    --ink: #161616;
    --navy: #1d3f86;
    --on-band: #ffffff;
    --edge: #d6d6dc;
  }
  * { box-sizing: border-box; margin: 0; padding: 0; }
  html, body { width: 1200px; height: 987px; overflow: hidden; }
  body { background: var(--bg); font-family: "Open Sans", Arial, sans-serif; position: relative; }

  .card {
    position: absolute;
    background: var(--card);
    border-radius: 26px;
    border: 1px solid var(--edge);
    overflow: hidden;
    box-shadow: 0 10px 28px rgba(0,0,0,0.10);
  }

  .brand { position: absolute; color: var(--ink); font-weight: 700; line-height: 1; }
  .brand-name { display: block; letter-spacing: -1px; white-space: nowrap; }
  .brand-sub { display: block; letter-spacing: 2px; white-space: nowrap; }

  /* Front */
  .card-front { left: 40px; top: 470px; width: 580px; height: 340px; }
  .front-band { position: absolute; left: 0; right: 0; top: 110px; height: 172px; background: var(--band); }
  .front-brand { left: 70px; top: 30px; text-align: right; }
  .front-brand .brand-name { font-size: 70px; }
  .front-brand .brand-sub { font-size: 22px; margin-top: 22px; }

  .contact { position: absolute; top: 160px; color: var(--on-band); font-size: 15px; line-height: 24px; }
  .contact-left { left: 40px; width: 215px; text-align: right; }
  .contact-right { left: 290px; }
  .contact-divider { position: absolute; left: 272px; top: 166px; width: 1px; height: 92px; background: rgba(255,255,255,0.75); }
  .contact-row { display: flex; align-items: center; gap: 8px; white-space: nowrap; }
  .contact-left .contact-row { justify-content: flex-end; }
  .contact-row svg { width: 15px; height: 15px; flex: none; }
  .social-mark { width: 13px; height: 13px; background: var(--on-band); border-radius: 2px; flex: none; }

  .tagline { position: absolute; left: 60px; top: 292px; font-family: "Courgette", cursive; color: var(--navy); font-size: 24px; letter-spacing: 2px; }

  /* Back */
  .card-back { left: 640px; top: 130px; width: 520px; height: 320px; }
  .programs { position: absolute; left: 34px; top: 26px; }
  .programs-title { color: var(--navy); font-weight: 600; font-size: 22px; margin-bottom: 4px; }
  .programs-list { list-style: none; color: #333; font-size: 15px; line-height: 22px; padding-left: 8px; }
  .programs-list li::before { content: "• "; }
  .back-brand { right: 36px; top: 148px; text-align: right; }
  .back-brand .brand-name { font-size: 48px; }
  .back-brand .brand-sub { font-size: 16px; margin-top: 8px; }
</style>
</head>
<body>

  <section class="card card-back" aria-label="Business card back">
    <div class="programs">
      <h2 class="programs-title">Program Offerings</h2>
      <ul class="programs-list">
        <li>Cosmetology</li>
        <li>Barber</li>
        <li>Spa Therapy</li>
        <li>Massage Therapy</li>
        <li>Makeup Artistry</li>
        <li>Skin Care</li>
        <li>Manicure</li>
        <li>Pedicure &amp; Nail Extensions</li>
        <li>Full Specialist</li>
      </ul>
    </div>
    <div class="brand back-brand">
      <span class="brand-name">Lumarove</span>
      <span class="brand-sub">ACADEMY</span>
    </div>
  </section>

  <section class="card card-front" aria-label="Business card front">
    <div class="front-band"></div>
    <div class="brand front-brand">
      <span class="brand-name">Lumarove</span>
      <span class="brand-sub">ACADEMY</span>
    </div>

    <div class="contact contact-left">
      <div class="contact-row">5126 NW 14th Avenue.</div>
      <div class="contact-row">Miami, Fl 33157</div>
      <div class="contact-row"><span class="social-mark"></span>/lumarovestyle</div>
      <div class="contact-row"><span class="social-mark"></span>/lumaroveacademy</div>
    </div>

    <div class="contact-divider"></div>

    <div class="contact contact-right">
      <div class="contact-row">
        <svg viewBox="0 0 16 16" aria-hidden="true"><circle cx="8" cy="8" r="7" fill="none" stroke="#fff" stroke-width="1.4"/><path d="M5.3 4.5l1.4 0 .6 1.8-.9.8a5 5 0 0 0 2.5 2.5l.8-.9 1.8.6v1.4c-3.5.4-6.6-2.7-6.2-6.2z" fill="#fff"/></svg>
        305-914-3062
      </div>
      <div class="contact-row">
        <svg viewBox="0 0 16 16" aria-hidden="true"><rect x="4" y="2" width="8" height="4" fill="#fff"/><rect x="1.5" y="6" width="13" height="6" rx="1" fill="#fff"/><rect x="4" y="10" width="8" height="4" fill="#fff" stroke="#b5479a" stroke-width="1"/></svg>
        786-552-4190
      </div>
      <div class="contact-row">
        <svg viewBox="0 0 16 16" aria-hidden="true" fill="none" stroke="#fff" stroke-width="1.2"><circle cx="8" cy="8" r="6.5"/><ellipse cx="8" cy="8" rx="3" ry="6.5"/><path d="M1.5 8h13M2.5 4.8h11M2.5 11.2h11"/></svg>
        www.lumaroveacademy.edu
      </div>
    </div>

    <div class="tagline">Beautify Your Future</div>
  </section>

</body>
</html>
```